Financial Services Company Needs New UI/UX

Hello!

We would like to see some UI/UX ideas for our software platform. I've attached a screen capture of our current "dashboard" (or main home page, essentially). We're looking for a very simple, clean, sleek design as there are many different pages throughout the system that will all need to coordinate. You can also view our website to see the colors and general "look" we have on there. It would be ideal for the portal to coordinate with the website since that is how they access the login page. Please submit your best ideas for the dashboard and we will reach out to our favorite designer to move forward with the rest of the pages. You can find our color hex codes on our website on the "Media" page. Should you need any other supporting logos or files please send us a message and we will try to accommodate.

Thanks!

Website: www.lendmarkbuilt.example

Target Market(s)

Our clients are contractors in the construction industry and our software helps them manage material purchases for their jobs.

Industry/Entity Type

Financial Service

Font styles to use
Sans Serif

Requirements
Must have
• The same content and language as the current dashboard but an updated look.
Should not have
• Too much distraction or busy patterns, we're looking for clean and simple and user friendly. Likely a solid or subtly textured background would be best.

```html
<!DOCTYPE html>
<html lang="en">
<head>
<meta charset="utf-8">
<title>Design Idea 03A – Dashboard</title>
<link rel="stylesheet" href="https://fonts.googleapis.com/css2?family=Open+Sans:wght@400;600;700&family=Saira+Semi+Condensed:wght@500&display=swap">
<style>
:root{
  --page:#2b2b2c;
  --title:#a593ef;
  --header:#3a3b40;
  --sidebar:#3b3b3d;
  --sidebar-line:#2c2c2e;
  --accent-red:#d0494b;
  --accent-orange:#e25f1a;
  --card:#4a8fd0;
  --card-head:#2f3035;
  --row-a:#e6e8f5;
  --row-b:#eee3e3;
  --col-head:#8a5a2b;
  --grid:#d3d3dc;
  --warn:#f5b800;
  --info:#f5b400;
  --ink:#222;
}
*{box-sizing:border-box;margin:0;padding:0}
html,body{width:1200px;height:1200px;overflow:hidden;background:var(--page)}
body{position:relative;font-family:"Open Sans",sans-serif;color:var(--ink)}
.board-title,.board-sub,.board-caption{position:absolute;left:0;width:1200px;text-align:center;font-family:"Saira Semi Condensed",sans-serif;font-weight:500;color:var(--title)}
.board-title{top:72px;font-size:34px;letter-spacing:1px}
.board-sub{top:124px;font-size:27px}
.board-caption{top:856px;left:0;width:1060px;font-size:28px}

.app{position:absolute;left:13px;top:197px;width:1160px;height:596px;overflow:hidden}
.app-backdrop{position:absolute;inset:0;background:linear-gradient(105deg,#c9d2ea 0%,#dfe5f3 45%,#e9e6dc 70%,#f2c233 82%,#e9aa18 100%)}
.topbar{position:absolute;left:0;top:0;width:1160px;height:55px;background:var(--header);color:#fff}
.brand{position:absolute;left:10px;top:9px;display:flex;align-items:center;gap:8px;font-size:20px;color:#fff}
.brand-dot{width:36px;height:36px;border-radius:50%;background:#2a7fd0}
.contact{position:absolute;top:18px;font-size:12px;display:flex;align-items:center;gap:6px}
.contact.phone{left:270px}
.contact.mail{left:448px}
.contact svg{width:18px;height:18px}
.user{position:absolute;left:912px;top:0;width:248px;height:55px;background:var(--accent-orange);display:flex;align-items:center;gap:14px;padding-left:22px;font-size:14px}
.avatar{width:32px;height:32px;border-radius:50%;background:radial-gradient(circle,#b08a6a,#5a3f2e);border:2px solid #f3e6dc}
.sidebar{position:absolute;left:0;top:55px;width:142px;height:455px;background:var(--sidebar)}
.nav-item{height:26px;display:flex;align-items:center;gap:10px;padding-left:16px;font-size:9px;color:#fff;border-bottom:1px solid var(--sidebar-line)}
.nav-item.active{background:var(--accent-red)}
.nav-item svg{width:14px;height:14px;fill:#fff}

.panel{position:absolute;left:152px;top:66px;width:851px;height:448px;background:#fff}
.dash-bar{position:absolute;left:6px;top:4px;width:842px;height:22px;background:var(--accent-red);color:#fff;font-size:11.5px;font-weight:700;display:flex;align-items:center;gap:8px;padding-left:10px}
.badge{display:inline-flex;width:12px;height:12px;border-radius:50%;background:var(--info);color:#fff;font-size:9px;font-weight:700;align-items:center;justify-content:center}
.badge.red{background:#e23a2a}
.legend{position:absolute;left:8px;top:32px;font-size:8.5px;color:#444;display:flex;align-items:center;gap:4px}
.legend .gap{width:6px}
.card{position:absolute;top:62px;width:176px;height:134px;background:var(--card);border-radius:0 0 3px 3px;color:#fff;text-align:center}
.card-head{height:27px;background:var(--card-head);display:flex;align-items:center;gap:8px;padding-left:10px;font-size:11.5px;font-weight:700}
.card-amount{margin-top:9px;font-size:19px;font-weight:700}
.card-note{font-size:7.5px;font-weight:700;line-height:10px;margin-top:5px}
.card-actions{position:absolute;left:0;right:0;bottom:14px;display:flex;justify-content:center;gap:10px}
.pill{background:#fff;color:#333;font-size:8px;font-weight:700;border-radius:9px;padding:3px 6px}
.tri{width:0;height:0;border-left:6px solid transparent;border-right:6px solid transparent;border-bottom:11px solid var(--warn)}
.block{position:absolute;top:216px;height:226px;border:1px solid var(--grid)}
.block-head{height:28px;background:var(--card-head);color:#fff;font-size:10.5px;font-weight:700;display:flex;align-items:center;gap:10px;padding-left:10px}
table{border-collapse:collapse;width:100%;table-layout:fixed;font-size:7.5px}
th{height:28px;color:var(--col-head);text-decoration:underline;font-weight:700;font-size:8.5px;background:#fff}
td{height:24.4px;text-align:center;border-right:1px solid var(--grid);line-height:9px}
th{border-right:1px solid var(--grid)}
tr:nth-child(odd) td{background:var(--row-a)}
tr:nth-child(even) td{background:var(--row-b)}
</style>
</head>
<body>
<div class="board-title">DESIGN IDEA - 03A</div>
<div class="board-sub">(Colors and fonts are changeable)</div>

<div class="app">
  <div class="app-backdrop" role="img" aria-label="Blueprint sheets with a hammer, tape measure and yellow hard hat"></div>

  <header class="topbar">
    <div class="brand"><span class="brand-dot"></span>LendmarkBuilt</div>
    <div class="contact phone">
      <svg viewBox="0 0 20 20"><circle cx="10" cy="10" r="9" fill="none" stroke="#e23a2a" stroke-width="1.5"/><path d="M6 5l2 0 1 3-1.5 1a6 6 0 0 0 3.5 3.5L12 11l3 1v2c-5 1-10-4-9-9z" fill="#e23a2a"/></svg>
      Support :&nbsp;&nbsp; 555-010-4477
    </div>
    <div class="contact mail">
      <svg viewBox="0 0 20 20"><circle cx="10" cy="10" r="9.5" fill="#f0a020"/><rect x="5" y="6.5" width="10" height="7" fill="#fff"/><path d="M5 6.5l5 4 5-4" fill="none" stroke="#f0a020" stroke-width="1"/></svg>
      support@harborlinesupply.example
    </div>
    <div class="user">
      <svg width="16" height="12" viewBox="0 0 16 12"><path d="M0 0h16L8 12z" fill="#fff"/></svg>
      <span class="avatar" role="img" aria-label="User profile photo"></span>
      <span>pc101@sample.example</span>
    </div>
  </header>

  <nav class="sidebar">
    <div class="nav-item active"><svg viewBox="0 0 16 16"><path d="M8 1l7 7h-2v6H10v-4H6v4H3V8H1z"/></svg>Home</div>
    <div class="nav-item"><svg viewBox="0 0 16 16"><path d="M2 12l6-6 2 2-6 6zM9 2l5 5-2 2-5-5z"/></svg>Job Center</div>
    <div class="nav-item"><svg viewBox="0 0 16 16"><path d="M1 4h14v8H1zM3 6v4h10V6z"/><circle cx="8" cy="8" r="1.6"/></svg>Payments</div>
    <div class="nav-item"><svg viewBox="0 0 16 16"><path d="M8 1l7 4H1zM2 6h2v6H2zM7 6h2v6H7zM12 6h2v6h-2zM1 13h14v2H1z"/></svg>Credit Management</div>
    <div class="nav-item"><svg viewBox="0 0 16 16"><path d="M3 1h7l3 3v11H3zM5 6h6v1H5zM5 9h6v1H5zM5 12h6v1H5z"/></svg>Prelien Center</div>
  </nav>

  <main class="panel">
    <div class="dash-bar"><span class="badge">?</span>DASHBOARD</div>
    <div class="legend"><span class="tri"></span>Indicates an Action is Required<span class="gap"></span><span class="badge">?</span>Information only - no action required</div>

    <section class="card" style="left:176px">
      <div class="card-head"><span class="badge red">i</span>Available Master Credit</div>
      <div class="card-amount">$1,29,500.00</div>
      <div class="card-note">Master Credit Limit : 250,000.00</div>
      <div class="card-actions"><span class="pill">Setup New Job</span></div>
    </section>
    <section class="card" style="left:361px">
      <div class="card-head"><span class="badge red">i</span>Last Payment</div>
      <div class="card-amount">$500.00</div>
      <div class="card-note">Last Payment Date : 6/28/2016</div>
      <div class="card-actions"><span class="pill">View Payments</span><span class="pill">View Billings</span></div>
    </section>
    <section class="card" style="left:546px">
      <div class="card-head"><span class="tri"></span>Next Payment</div>
      <div class="card-amount">$158.95</div>
      <div class="card-note">Due Date : 6/28/2016<br>Current Principle : $9,968.46<br>Minimum Interest/Fees : &nbsp;$158.95</div>
      <div class="card-actions"><span class="pill">Make Payment</span></div>
    </section>

    <section class="block" style="left:6px;width:413px">
      <div class="block-head"><svg width="14" height="16" viewBox="0 0 14 16"><rect x="1" y="1" width="12" height="14" rx="1" fill="none" stroke="#d0494b" stroke-width="1.5"/><path d="M3.5 5h7M3.5 8h7M3.5 11h7" stroke="#d0494b"/></svg>Task Summary</div>
      <table>
        <colgroup><col style="width:23px"><col style="width:156px"><col style="width:140px"><col></colgroup>
        <tr><th></th><th>Task</th><th>Status</th><th>Received</th></tr>
        <tr><td><span class="badge">?</span></td><td>Supplier Invoice</td><td>Confirmation by Account Manager<br>Pending</td><td>5/1/2016</td></tr>
        <tr><td></td><td></td><td></td><td></td></tr>
        <tr><td></td><td></td><td></td><td></td></tr>
        <tr><td></td><td></td><td></td><td></td></tr>
        <tr><td></td><td></td><td></td><td></td></tr>
        <tr><td></td><td></td><td></td><td></td></tr>
        <tr><td></td><td></td><td></td><td></td></tr>
      </table>
    </section>

    <section class="block" style="left:433px;width:414px">
      <div class="block-head"><svg width="16" height="16" viewBox="0 0 16 16"><path d="M2 13l7-7 2 2-7 7zM9 1l6 6-2 2-6-6z" fill="#f0b020"/></svg>Active Jobs</div>
      <table>
        <colgroup><col style="width:76px"><col style="width:94px"><col style="width:78px"><col style="width:85px"><col></colgroup>
        <tr><th>Job#</th><th>Job Name</th><th>Status</th><th>Credit Limit</th><th>Avail. Credit</th></tr>
        <tr><td>pc101-001</td><td>Job#001</td><td>Active</td><td>$50,100.00</td><td>$35,100.00</td></tr>
        <tr><td>pc101-002</td><td>Job#002</td><td>Active</td><td>$40,000.00</td><td>$2,00.00</td></tr>
        <tr><td>pc101-003</td><td>Job#003</td><td>Active</td><td>$22,000.00</td><td>$0.00</td></tr>
        <tr><td>pc101-004</td><td>Job#004</td><td>Active</td><td>$10,400.00</td><td>$10,400.00</td></tr>
        <tr><td></td><td></td><td></td><td></td><td></td></tr>
        <tr><td></td><td></td><td></td><td></td><td></td></tr>
        <tr><td></td><td></td><td></td><td></td><td></td></tr>
      </table>
    </section>
  </main>
</div>

<div class="board-caption">New Dashboard &nbsp;(With Old Background Image)</div>
</body>
</html>
```